Business Card: RW Office Partners - Your tidy answer finder

Business Name: RW Office Partners
Website: www.rwofficepartners.com.au
Email: marisol@rwofficepartners.com.au
Mobile: 61 487 902 346
Facebook: @rwofficepartners
Instrgram: @rwofficepartners

Brading Colours:
HEX
#986474
#ddccd3
#7a8498
#c9d8e4
#000000
#ffffff

Tag Line: Your organised problem solver

Link to DRAFT website:
https://helpdeskhub.sitebuilderx.com/rw-office-partners

About Page from the website:
My name is Marisol Bramwell, and I would love to assist you to become more productive in your day to day and achieve your business and personal goals.
My mission is to give you time, time to work on the important tasks of your business or to be able to spend more time with your family. I will take on the tasks you don’t have time for, don’t know well or simply don’t like to do.
I have an extensive background in Administration, Tender Coordination, Document Control, WHS and Quality Management working primarily in the Construction, Mining and Corporate World.
I am passionate about being organised, having order and making things in your life (and mine) easier! I love to watch something unfold and grow into something amazing! I am known for being the go-to problem solver, the organiser of all things, producing high standards of work even under pressure. I’m also a confident communicator, and I understand that you’re busy running your business.

Target Market(s)

Small to Medium Business who require assistance in their business by a virtual assistant.

Industry/Entity Type

Virtual Assistant

Contact Information for Business Card

Mobile: 61 487 902 346

Font styles to use
Sans Serif

Colors
ffffff

Requirements
Must have
• Branding Colours as outlined.
Contact Details as outlined.
Logo as provided.
Proper contact details - mobile, facebook, instragm, website.
Simple, Elegant, very clean looking.
Should not have
• Note cute with pictures.
Not too girly as still want to market to construction companies.

```html
<!DOCTYPE html>
<html lang="en">
<head>
<meta charset="utf-8">
<title>RW Office Partners – Business Card</title>
<link href="https://fonts.googleapis.com/css2?family=Roboto:wght@400;500&display=swap" rel="stylesheet">
<style>
  :root {
    --mauve: #986474;
    --slate: #7a8498;
    --ink: #4a4f5a;
    --paper: #ffffff;
    --backdrop: #d6d6d4;
  }
  * { box-sizing: border-box; margin: 0; padding: 0; }
  html, body { width: 1200px; height: 801px; overflow: hidden; }
  body {
    background: var(--backdrop);
    font-family: "Roboto", Arial, sans-serif;
    position: relative;
  }
  .card {
    position: absolute;
    top: 252px;
    width: 520px;
    height: 297px;
    overflow: hidden;
    box-shadow: 0 6px 18px rgba(0,0,0,0.18);
  }
  .card--front { left: 50px; background: var(--paper); }
  .card--back  { left: 630px; background: var(--slate); }

  .card__band { position: absolute; inset: 0; width: 100%; height: 100%; }

  .brand {
    position: absolute;
    left: 34px;
    top: 112px;
    width: 200px;
    color: var(--slate);
    font-weight: 500;
    font-size: 26px;
    line-height: 1.05;
    letter-spacing: 1px;
    text-transform: uppercase;
  }
  .divider {
    position: absolute;
    left: 246px;
    top: 92px;
    width: 1px;
    height: 100px;
    background: var(--mauve);
  }
  .contacts {
    position: absolute;
    left: 260px;
    top: 94px;
    list-style: none;
    color: var(--ink);
    font-size: 13px;
    line-height: 24px;
  }
  .contacts li { display: flex; align-items: center; gap: 6px; white-space: nowrap; }
  .contacts svg { width: 11px; height: 11px; flex: none; }
  .social-dot {
    width: 9px; height: 9px; border-radius: 50%;
    background: var(--slate); flex: none;
  }
  .tagline {
    position: absolute;
    right: 22px;
    bottom: 14px;
    color: var(--paper);
    font-size: 13px;
    letter-spacing: 0.3px;
  }
  .back-name {
    position: absolute;
    right: 40px;
    bottom: 84px;
    color: var(--paper);
    font-weight: 500;
    font-size: 22px;
    letter-spacing: 1px;
    text-transform: uppercase;
  }
</style>
</head>
<body>

<section class="card card--front" aria-label="Business card front">
  <svg class="card__band" viewBox="0 0 520 297" preserveAspectRatio="none" aria-hidden="true">
    <path d="M0,297 C160,280 330,210 520,186 L520,192 C340,214 180,286 30,297 Z" fill="var(--mauve)"/>
    <path d="M70,297 C220,282 360,222 520,204 L520,297 Z" fill="var(--slate)"/>
  </svg>

  <div class="brand">RW Office<br>Partners</div>
  <div class="divider"></div>

  <ul class="contacts">
    <li>
      <svg viewBox="0 0 12 12"><circle cx="6" cy="6" r="6" fill="var(--mauve)"/><path d="M4 3.2l1 1.4-.6.7c.4.8 1 1.4 1.8 1.8l.7-.6 1.4 1-.6 1.2C5.6 8.5 3.5 6.4 3.3 3.8z" fill="#fff"/></svg>
      61 487 902 346
    </li>
    <li>
      <svg viewBox="0 0 12 12"><rect x="0.5" y="2" width="11" height="8" rx="1" fill="var(--mauve)"/><path d="M1 2.6l5 3.6 5-3.6" stroke="#fff" stroke-width="0.9" fill="none"/></svg>
      marisol@rwofficepartners.com.au
    </li>
    <li>
      <svg viewBox="0 0 12 12"><circle cx="6" cy="6" r="5.5" fill="var(--mauve)"/><path d="M0.8 6h10.4M6 0.6c-2.4 2.8-2.4 8 0 10.8M6 0.6c2.4 2.8 2.4 8 0 10.8" stroke="#fff" stroke-width="0.8" fill="none"/></svg>
      www.rwofficepartners.com.au
    </li>
    <li>
      <span class="social-dot"></span>
      @rwofficepartners
    </li>
  </ul>

  <p class="tagline">Your tidy answer finder</p>
</section>

<section class="card card--back" aria-label="Business card back">
  <p class="back-name">RW Office Partners</p>
</section>

</body>
</html>
```